Building and constructions

Extension, additions, alterations, renovations, new homes, project management and supervision

Industry/Entity Type

Building

Contact Information for Business Card

Tolvane building service constructions PTY LTD
Marcus Delveno builder/ supervisor
BLD 71940 member of RHG
0412735190 email tmrk41@qelmora.com

```html
<!DOCTYPE html>
<html lang="en">
<head>
<meta charset="utf-8">
<title>Tolvane building service constructions – business card</title>
<link rel="stylesheet" href="https://fonts.googleapis.com/css2?family=Tinos:wght@400;700&display=swap">
<style>
  :root {
    --page: #e7e4e0;
    --orange-light: #f08a4c;
    --orange: #ea6a2e;
    --orange-deep: #d9411a;
    --orange-edge: #c8501f;
    --charcoal: #161616;
    --black: #0b0b0b;
    --grey-light: #8b9094;
    --grey-dark: #3f4549;
    --white: #ffffff;
    --name-orange: #f2884c;
    --sky: #9fb4c8;
    --wall: #d9d4cc;
    --lawn: #6f9a52;
    --pool: #46a8c9;
  }
  * { box-sizing: border-box; margin: 0; padding: 0; }
  html, body { width: 1200px; height: 913px; overflow: hidden; }
  body {
    background: var(--page);
    font-family: "Tinos", "Times New Roman", serif;
    position: relative;
  }
  .card {
    position: absolute;
    left: 250px;
    width: 700px;
    height: 400px;
    overflow: hidden;
    box-shadow: 0 6px 18px rgba(0,0,0,.18);
  }
  /* ---------- front ---------- */
  .card--front { top: 40px; background: linear-gradient(160deg, var(--orange-light), var(--orange) 45%, var(--orange-deep)); }
  .front__photo-band {
    position: absolute; left: 0; top: 0; width: 100%; height: 160px;
    background: linear-gradient(100deg, var(--grey-dark), var(--grey-light) 55%, #6d7377);
  }
  .front__divider {
    position: absolute; left: 0; top: 160px; width: 100%; height: 8px;
    background: var(--orange-edge);
  }
  .front__name {
    position: absolute; left: 250px; top: 86px;
    font-size: 30px; color: var(--name-orange); font-weight: 400;
  }
  .front__role {
    position: absolute; left: 262px; top: 124px;
    font-size: 20px; color: var(--white);
  }
  .project-photo {
    position: absolute; width: 120px; height: 120px; border-radius: 50%;
    background: linear-gradient(180deg, var(--sky) 0%, var(--wall) 45%, #bfb7ac 75%, var(--lawn) 100%);
    border: 2px solid rgba(255,255,255,.55);
  }
  .project-photo--1 { left: 110px; top: 240px; }
  .project-photo--2 { left: 330px; top: 210px; background: linear-gradient(180deg, #6f7fd0 0%, #c9cbe8 40%, #8a8fb4 75%, #5a6a8a 100%); }
  .project-photo--3 { left: 540px; top: 180px; }
  /* ---------- back ---------- */
  .card--back { top: 473px; background: var(--black); }
  .back__panel {
    position: absolute; left: 0; top: 0; width: 330px; height: 100%;
    background: linear-gradient(165deg, var(--orange-light), var(--orange) 45%, var(--orange-deep));
  }
  .back__company {
    position: absolute; left: 32px; top: 44px; width: 280px;
    font-size: 21px; line-height: 1.2; color: var(--white);
  }
  .back__rule {
    position: absolute; left: 0; top: 112px; width: 330px; height: 2px;
    background: var(--orange-edge);
  }
  .back__dark {
    position: absolute; left: 330px; top: 0; right: 0; bottom: 0;
    background: linear-gradient(160deg, #2a2a2a, var(--charcoal) 40%, var(--black));
  }
  .contact-tab {
    position: absolute; right: 0; height: 40px;
    background: var(--orange); border-radius: 20px 0 0 20px;
    display: flex; align-items: center; padding-left: 14px;
  }
  .contact-tab--phone { top: 26px; width: 110px; }
  .contact-tab--email { top: 80px; width: 70px; }
  .contact-tab__icon {
    width: 28px; height: 28px; border-radius: 50%; border: 2px solid var(--white);
    display: flex; align-items: center; justify-content: center;
    color: var(--white); font-size: 18px; font-weight: 700; line-height: 1;
  }
  .back__contact {
    position: absolute; left: 356px; top: 66px;
    font-size: 22px; line-height: 2.4; color: var(--white);
  }
  .back__photo {
    position: absolute; left: 530px; top: 148px; width: 120px; height: 120px; border-radius: 50%;
    background: linear-gradient(180deg, var(--sky) 0%, #e1ddd5 45%, #b9b3aa 65%, var(--pool) 100%);
    border: 2px solid rgba(255,255,255,.5);
  }
  .back__licence {
    position: absolute; left: 546px; top: 284px;
    font-size: 19px; line-height: 1.25; color: var(--white);
  }
</style>
</head>
<body>
  <section class="card card--front" aria-label="Business card front">
    <div class="front__photo-band" role="img" aria-label="Photo of a finished home exterior with veranda"></div>
    <div class="front__divider"></div>
    <h1 class="front__name">Marcus Delveno</h1>
    <p class="front__role">Builder/ Supervisor</p>
    <div class="project-photo project-photo--1" role="img" aria-label="Photo of a two-storey house"></div>
    <div class="project-photo project-photo--2" role="img" aria-label="Photo of a new home render"></div>
    <div class="project-photo project-photo--3" role="img" aria-label="Photo of a house with lawn"></div>
  </section>

  <section class="card card--back" aria-label="Business card back">
    <div class="back__panel"></div>
    <p class="back__company">Tolvane building service constructions PTY LTD</p>
    <div class="back__rule"></div>
    <div class="back__dark"></div>
    <div class="contact-tab contact-tab--phone">
      <span class="contact-tab__icon">
        <svg width="16" height="16" viewBox="0 0 24 24" aria-hidden="true"><path fill="#fff" d="M6.6 10.8a15.1 15.1 0 0 0 6.6 6.6l2.2-2.2c.3-.3.7-.4 1-.2 1.1.4 2.3.6 3.6.6.6 0 1 .4 1 1V20c0 .6-.4 1-1 1A17 17 0 0 1 3 4c0-.6.4-1 1-1h3.5c.6 0 1 .4 1 1 0 1.3.2 2.5.6 3.6.1.3 0 .7-.2 1z"/></svg>
      </span>
    </div>
    <div class="contact-tab contact-tab--email"><span class="contact-tab__icon">@</span></div>
    <p class="back__contact">0412735190<br>tmrk41@qelmora.com</p>
    <div class="back__photo" role="img" aria-label="Photo of a home with swimming pool"></div>
    <p class="back__licence">BLD 71940<br>member of RHG</p>
  </section>
</body>
</html>
```